Corrigan Architecture (business card)

We need a business card design. We are a full service architectural firm that specializes in mostly residential projects and some commercial projects. We are located in Hudson Valley, New York. We work with high end clients and want a business card that is memorable and has a sleek, modern, design but will not go out of style (timeless).

Target Market(s)

high end residential clients

Industry/Entity Type

Architect

Contact Information for Business Card

Front of card
Company Logo
website: www.corriganarchitectur.example
what we do: residential, Commercial

back of card
Owner's Name: Dorian Corrigan
owner's title: Principal
Business address: 2873 Route 92 Suite A, Brellfordton, NY 12688
phone number: 845-608-2917
e-mail: dc@corriganarchitecture.example

We like:
icons
sleek and clean design
simple not too busy or too much text

Font styles to use
Sans Serif

Colors
0356a4

Requirements
Must have
• company colors are navy blue, white, and gray
• Front of card
• Company Logo
• website: www.corriganarchitectur.example
• what we do: residential, Commercial
• back of card
• Owner's Name: Dorian Corrigan
• owner's title: Principal
• Business address: 2873 Route 92 Suite A, Brellfordton, NY 12688
• phone number: 845-608-2917
• e-mail: dc@corriganarchitecture.example
Nice to have
• We like:
• icons
• sleek and clean design
• simple not too much text
• color of the card to be either blue or gray
Should not have
• we do not like houses in the design or plans of houses-this is over done and we don't like it.
• no QR CODES

```html
<!DOCTYPE html>
<html lang="en">
<head>
<meta charset="utf-8">
<title>Corrigan Architecture — Business Card</title>
<link href="https://fonts.googleapis.com/css2?family=Jost:wght@300;400&family=Barlow:wght@400;600;700&display=swap" rel="stylesheet">
<style>
  :root {
    --navy: #25205f;
    --navy-deep: #1f1b55;
    --band-light: #e4e4e8;
    --paper: #ffffff;
    --paper-shade: #ececee;
    --ink: #3d3d45;
    --gray-text: #9a9aa8;
    --backdrop: #d3d3d5;
  }
  * { margin: 0; padding: 0; box-sizing: border-box; }
  html, body {
    width: 1200px; height: 900px; overflow: hidden;
    background: var(--backdrop);
  }
  .sheet {
    position: relative; width: 1200px; height: 900px;
    display: flex; flex-direction: column; align-items: center;
    justify-content: center; gap: 42px;
  }
  .card {
    position: relative; width: 680px; height: 389px; overflow: hidden;
    box-shadow: 0 6px 14px rgba(0,0,0,0.18);
  }

  /* Front */
  .card--front {
    background: linear-gradient(160deg, var(--navy-deep), var(--navy));
  }
  .card--front .band {
    position: absolute; top: 0; bottom: 0; left: 168px; width: 46px;
    background: var(--band-light);
  }
  .front-identity {
    position: absolute; left: 300px; top: 120px; color: #d9d9e4;
    font-family: "Jost", sans-serif;
  }
  .front-identity .firm-name {
    font-weight: 300; font-size: 38px; line-height: 1.0;
    letter-spacing: 1px; text-transform: uppercase;
  }
  .front-identity .services {
    margin-top: 12px; font-family: "Barlow", sans-serif; font-weight: 400;
    font-size: 15px; letter-spacing: 3.2px; color: #b8b8cc;
    text-transform: uppercase;
  }
  .front-identity .services .dot { margin: 0 6px; }
  .website {
    position: absolute; left: 300px; bottom: 70px;
    font-family: "Barlow", sans-serif; font-size: 17px; color: #e6e6ef;
    letter-spacing: 0.6px;
  }
  .website strong { font-weight: 700; }

  /* Back */
  .card--back {
    background: linear-gradient(180deg, var(--paper-shade), var(--paper) 45%);
  }
  .card--back .band {
    position: absolute; top: 0; bottom: 0; left: 478px; width: 34px;
    background: var(--navy);
  }
  .back-content {
    position: absolute; left: 58px; top: 60px;
    font-family: "Barlow", sans-serif; color: var(--ink);
  }
  .wordmark {
    display: flex; align-items: center; gap: 12px;
  }
  .wordmark .mark-square {
    width: 30px; height: 30px; background: var(--navy);
  }
  .wordmark .wordmark-text {
    font-family: "Jost", sans-serif; font-weight: 300; font-size: 30px;
    line-height: 1.0; color: var(--navy); text-transform: uppercase;
    letter-spacing: 0.8px;
  }
  .person { margin-top: 48px; }
  .person .name {
    font-weight: 700; font-size: 22px; color: var(--navy);
  }
  .person .title {
    font-size: 16px; color: #6e6e78; margin-top: 1px;
  }
  .contact {
    margin-top: 30px; font-size: 15.5px; line-height: 1.42; color: var(--ink);
  }
  .contact .line { display: flex; align-items: center; gap: 8px; }
  .contact svg { width: 14px; height: 14px; flex: none; }
</style>
</head>
<body>
<main class="sheet">
  <section class="card card--front" aria-label="Card front">
    <div class="band"></div>
    <div class="front-identity">
      <div class="firm-name">Corrigan<br>Architecture</div>
      <div class="services">Residential<span class="dot">•</span>Commercial</div>
    </div>
    <div class="website">www.<strong>corriganarchitectur</strong>.example</div>
  </section>

  <section class="card card--back" aria-label="Card back">
    <div class="band"></div>
    <div class="back-content">
      <div class="wordmark">
        <span class="mark-square"></span>
        <span class="wordmark-text">Corrigan<br>Architecture</span>
      </div>
      <div class="person">
        <div class="name">Dorian Corrigan</div>
        <div class="title">Principal</div>
      </div>
      <div class="contact">
        <div class="line">2873 Route 92 Suite A</div>
        <div class="line">Brellfordton, NY 12688</div>
        <div class="line">
          <svg viewBox="0 0 24 24" aria-hidden="true"><path fill="#25205f" d="M6.6 10.8a15.1 15.1 0 0 0 6.6 6.6l2.2-2.2c.3-.3.7-.4 1-.2 1.1.4 2.3.6 3.6.6.6 0 1 .4 1 1V20c0 .6-.4 1-1 1A17 17 0 0 1 3 4c0-.6.4-1 1-1h3.5c.6 0 1 .4 1 1 0 1.3.2 2.5.6 3.6.1.3 0 .7-.2 1z"/></svg>
          845-608-2917
        </div>
        <div class="line">
          <svg viewBox="0 0 24 24" aria-hidden="true"><rect x="2.5" y="5" width="19" height="14" fill="none" stroke="#25205f" stroke-width="2.2"/><path d="M3 6l9 7 9-7" fill="none" stroke="#25205f" stroke-width="2.2"/></svg>
          dc@corriganarchitecture.example
        </div>
      </div>
    </div>
  </section>
</main>
</body>
</html>
```